Harbor Light Campaign Website & Materials

Project Overview:

We are running a community-focused campaign that emphasizes unity and inclusivity for our people. Instead of a candidate-centric “Vote Larkin” branding, our campaign will feature a message that rallies all community members: “Vote for the People. Vote for Our Community. Vote for Our Families & Children. Vote for a Team that Represents Everyone.” Our goal is to build trust, transparency, and collaboration by engaging every eligible member of the Okemasi Wendaku Nation in the electoral process.

```html
<!DOCTYPE html>
<html lang="en">
<head>
<meta charset="utf-8">
<title>Harbor Light Campaign</title>
<link rel="stylesheet" href="https://fonts.googleapis.com/css2?family=Montserrat:wght@500;600;700;800&family=Roboto:wght@400;500&display=swap">
<style>
:root{
  --red:#d7141c;
  --navy:#2f3a4f;
  --ink:#1b1b1b;
  --text:#333;
  --light:#e9ecf1;
  --white:#fff;
  --sky:#9cc3ee;
}
*{box-sizing:border-box;margin:0;padding:0}
html,body{width:1200px;height:3822px;overflow:hidden}
body{position:relative;background:var(--white);font-family:Roboto,Arial,sans-serif;color:var(--text)}
.abs{position:absolute}
.head{font-family:Montserrat,Arial,sans-serif;font-weight:700;color:var(--ink);text-transform:uppercase}
.red{color:var(--red)}
.btn{position:absolute;background:var(--red);color:#fff;font-family:Montserrat,Arial,sans-serif;font-weight:700;text-transform:uppercase;display:flex;align-items:center;justify-content:center;border:2px solid #fff;box-shadow:0 0 0 1px var(--red)}
.rule{position:absolute;height:3px;width:55px;background:var(--ink)}
.ph{position:absolute}

/* header */
.site-header{position:absolute;left:0;top:0;width:1200px;height:80px;background:#fff}
.logo{position:absolute;left:150px;top:24px;font-family:Montserrat,sans-serif;font-weight:700;font-size:25px;color:var(--ink);letter-spacing:.5px}
.nav a{position:absolute;top:31px;font-family:Montserrat,sans-serif;font-weight:500;font-size:13.5px;color:var(--ink);text-decoration:none}
.nav .active{top:24px;left:424px;width:67px;height:31px;background:var(--red);color:#fff;display:flex;align-items:center;justify-content:center;font-weight:700}
.lang{position:absolute;left:974px;top:24px;width:79px;height:31px;border:1px solid #999;font-size:12px;display:flex;align-items:center;justify-content:center;gap:6px;color:var(--ink)}
.lang i{width:16px;height:10px;background:linear-gradient(#b22 50%,#fff 50%);display:block}

/* hero */
.hero{position:absolute;left:0;top:80px;width:1200px;height:662px;background:linear-gradient(180deg,#7fb0e8 0%,#b9d6f3 55%,#cfe0ef 100%);overflow:hidden}
.hero .building{position:absolute;left:100px;top:60px;width:1000px;height:602px;background:linear-gradient(180deg,rgba(120,110,90,0) 0%,rgba(120,110,90,0) 45%,#6d6554 75%,#4b4a44 100%)}
.vote{position:absolute;font-family:Montserrat,sans-serif;font-weight:700;font-size:20px;line-height:25px;color:var(--navy);text-transform:uppercase}
.vote.r{text-align:right}
.badge{position:absolute;width:60px;height:60px;border-radius:50%;background:var(--red)}

/* welcome */
.welcome h2{position:absolute;left:655px;top:798px;font-size:31px;line-height:41px}
.body-copy{position:absolute;font-size:14.5px;line-height:21px;color:var(--text)}
.body-copy p+p{margin-top:21px}

/* candidate */
.candidates{position:absolute;left:0;top:1330px;width:1200px;height:562px;background:var(--navy)}
.sec-title{position:absolute;left:0;width:1200px;text-align:center;font-family:Montserrat,sans-serif;font-weight:700;font-size:30px;text-transform:uppercase}
.card{position:absolute;top:1467px;width:213px}
.card .ph{position:relative;width:213px;height:201px}
.card h3{font-family:Montserrat,sans-serif;font-weight:800;font-size:14.5px;color:#fff;margin-top:24px;white-space:nowrap}
.card .role{font-family:Roboto,sans-serif;font-weight:500;font-size:12px;color:#fff;margin-top:5px}
.card p{font-size:12px;line-height:18px;color:#d8dce4;margin-top:9px;height:54px}
.card .btn{position:relative;width:99px;height:29px;font-size:11.5px;margin:16px 0 0 3px}

/* engagement */
.engage{position:absolute;left:0;top:1892px;width:1200px;height:480px;background:var(--light)}
.engage .photo{position:absolute;left:590px;top:0;width:610px;height:450px;background:linear-gradient(90deg,var(--light) 0%,#a9b48f 25%,#7f8f63 55%,#5c6a4a 100%)}

/* news */
.news-card{position:absolute;top:2560px;width:286px;height:415px;border:1px solid #bbb;background:#fff}
.news-card .ph{position:relative;width:284px;height:193px}
.news-card .date{position:absolute;left:22px;top:172px;background:#fff;padding:0 12px;height:28px;line-height:30px;font-size:14px;color:var(--ink)}
.news-card h3{font-family:Montserrat,sans-serif;font-weight:700;font-size:13.5px;line-height:19px;color:var(--ink);margin:22px 28px 0}
.news-card p{font-size:13px;line-height:18px;margin:10px 28px 0;color:#333}
.news-card .btn{position:relative;width:100px;height:30px;font-size:12px;margin:14px 0 0 31px}

/* cta */
.cta{position:absolute;left:0;top:3031px;width:1200px;height:360px;background:linear-gradient(180deg,#3a4662 0%,#3c4964 60%,#4a5672 100%)}
.cta h2{position:absolute;left:0;top:64px;width:1200px;text-align:center;font-family:Montserrat,sans-serif;font-weight:800;font-size:30px;line-height:41px;color:#fff;text-transform:uppercase}
.cta p{position:absolute;left:0;top:155px;width:1200px;text-align:center;font-size:18px;color:#fff}

/* footer */
.footer{position:absolute;left:0;top:3340px;width:1200px;height:482px;background:var(--light)}
.f-logo{position:absolute;left:147px;top:3434px;font-family:Montserrat,sans-serif;font-weight:600;font-size:35px;color:var(--navy)}
.f-nav a{position:absolute;top:3521px;font-family:Montserrat,sans-serif;font-weight:600;font-size:13px;color:var(--ink);text-decoration:none}
.contact-item{position:absolute;top:3585px;display:flex;align-items:center;gap:15px}
.contact-item .ic{width:36px;height:36px;border-radius:50%;background:var(--navy);display:flex;align-items:center;justify-content:center}
.contact-item span{font-family:Montserrat,sans-serif;font-weight:500;font-size:16px;line-height:21px;color:var(--ink)}
.social{position:absolute;top:3698px;width:24px;height:24px;border-radius:50%;background:var(--navy)}
</style>
</head>
<body>

<header class="site-header">
  <div class="logo">HARBOR LIGHT</div>
  <nav class="nav">
    <a class="active">HOME</a>
    <a style="left:510px">ABOUT</a>
    <a style="left:587px">CANDIDATE</a>
    <a style="left:697px">COMMUNITY</a>
    <a style="left:816px">NEWS</a>
    <a style="left:881px">CONTACT</a>
  </nav>
  <div class="lang"><i></i>EN ▾</div>
</header>

<section class="hero">
  <div class="building" role="img" aria-label="Parliament building with clock tower under a clear blue sky"></div>
  <div class="vote r" style="right:675px;top:112px">Vote for<br><span class="red">the people</span></div>
  <div class="badge" style="left:550px;top:108px"></div>
  <div class="vote" style="left:825px;top:98px">Vote for a <span class="red">team</span><br>that represents<br>everyone.</div>
  <div class="badge" style="left:738px;top:101px"></div>
  <div class="vote r" style="right:709px;top:237px">Vote for our<br><span class="red">families &amp; children</span></div>
  <div class="badge" style="left:513px;top:234px"></div>
  <div class="vote" style="left:869px;top:246px">Vote for our<br><span class="red">community</span></div>
  <div class="badge" style="left:789px;top:240px"></div>
  <svg class="abs" style="left:0;top:0" width="1200" height="662" viewBox="0 0 1200 662" aria-hidden="true">
    <g fill="#fff">
      <circle cx="580" cy="128" r="8"/><path d="M566 152a14 12 0 0 1 28 0z"/>
      <circle cx="768" cy="123" r="5"/><circle cx="758" cy="128" r="4"/><circle cx="778" cy="128" r="4"/>
      <rect x="763" y="130" width="10" height="14" rx="3"/><rect x="754" y="134" width="8" height="11" rx="3"/><rect x="774" y="134" width="8" height="11" rx="3"/>
      <circle cx="543" cy="256" r="5"/><circle cx="531" cy="260" r="4"/><circle cx="555" cy="260" r="4"/>
      <rect x="538" y="262" width="10" height="16" rx="3"/><rect x="527" y="266" width="8" height="12" rx="3"/><rect x="551" y="266" width="8" height="12" rx="3"/>
      <circle cx="819" cy="262" r="5"/><circle cx="807" cy="266" r="4"/><circle cx="831" cy="266" r="4"/>
      <rect x="814" y="268" width="10" height="16" rx="3"/><rect x="803" y="272" width="8" height="12" rx="3"/><rect x="827" y="272" width="8" height="12" rx="3"/>
    </g>
    <path d="M0 590 C150 690 420 690 700 620 S1060 560 1200 580 L1200 662 L0 662Z" fill="#fff"/>
    <path d="M0 600 C140 705 420 705 700 630 S1060 570 1200 588" fill="none" stroke="#2f3a4f" stroke-width="9"/>
  </svg>
</section>

<section class="welcome">
  <div class="ph" style="left:151px;top:802px;width:463px;height:420px;background:linear-gradient(180deg,#3f6fb0 0%,#9ab6d8 35%,#2c3a2a 46%,#dfe3e8 60%,#f3f4f6 100%)" role="img" aria-label="Snow-covered river bank with pine forest under a cloudy sky"></div>
  <h2 class="head">Welcome to your<br><span class="red">community campaign</span></h2>
  <div class="rule" style="left:657px;top:892px"></div>
  <div class="body-copy" style="left:657px;top:925px;width:400px">
    <p>This is more than an election — it's a movement rooted in unity, trust, and belonging. Our goal is to ensure every voice in the Okemasi Wendaku Nation is heard and respected. We believe in fair, transparent elections that reflect the true will of the people.</p>
    <p>Together, we're building a future grounded in <span class="red" style="font-weight:500">accountability, cultural revitalization, and community empowerment</span> — where families thrive, traditions are honored, and leadership is shared. This campaign is not about one person — it's about all of us.</p>
  </div>
  <div class="btn" style="left:658px;top:1183px;width:115px;height:36px;font-size:14px">Read more</div>
</section>

<svg class="abs" style="left:0;top:1280px" width="1200" height="60" viewBox="0 0 1200 60" aria-hidden="true">
  <path d="M0 60 L0 56 C300 10 700 0 1200 50 L1200 60Z" fill="#2f3a4f"/>
  <path d="M0 56 C300 10 700 0 1200 50" fill="none" stroke="#d7141c" stroke-width="6"/>
</svg>
<section class="candidates">
  <div class="sec-title" style="top:24px;color:#fff">Candidate</div>
  <div class="rule" style="left:573px;top:84px;background:#fff"></div>
</section>
<div class="card" style="left:150px">
  <div class="ph" style="background:linear-gradient(180deg,#6fa2d8 0%,#2f5a2e 35%,#2d4f7a 60%,#9a8e80 100%)" role="img" aria-label="Rocky lakeshore with evergreen trees"></div>
  <h3>DANA WHITFIELD</h3><div class="role">Candidate for Councillor</div>
  <p>My name is Dana Whitfield, and I am honoured to put my name forward as a candidate</p>
  <div class="btn">Read more</div>
</div>
<div class="card" style="left:380px">
  <div class="ph" style="background:linear-gradient(180deg,#6b6f73 0%,#3c4350 60%,#2a3040 100%)" role="img" aria-label="Portrait of candidate in a dark suit"></div>
  <h3>RENEE CALDER</h3><div class="role">Candidate for Resix</div>
  <p>My name is Renee Calder, River Song Woman. I am honoured to accept my nomination</p>
  <div class="btn">Read more</div>
</div>
<div class="card" style="left:608px">
  <div class="ph" style="background:linear-gradient(90deg,#3a3430 0%,#1e1b1a 50%,#a44a1c 100%)" role="img" aria-label="Portrait of member against a patterned backdrop"></div>
  <h3>WREN</h3><div class="role">Member</div>
  <p>I am writing to you with a heartfelt hope that we can uphold our community's unity and ensure a</p>
  <div class="btn">Read more</div>
</div>
<div class="card" style="left:838px">
  <div class="ph" style="background:linear-gradient(135deg,#6f8a4f 0%,#c9b8a6 50%,#e0701e 100%)" role="img" aria-label="Portrait of member outdoors wearing sunglasses"></div>
  <h3>LOUISE MARCHAND OSTREY</h3><div class="role">Member</div>
  <p>Lorem Ipsum is simply dummy text of the printing nd typesetting industry. Lorem Ipsum has been the</p>
  <div class="btn">Read more</div>
</div>

<section class="engage">
  <div class="photo" role="img" aria-label="Smiling group of diverse community members outdoors"></div>
  <h2 class="head abs" style="left:157px;top:76px;font-size:30px">Community engagement</h2>
  <div class="rule" style="left:158px;top:136px"></div>
  <div class="body-copy" style="left:158px;top:176px;width:415px">Lorem ipsum dolor sit amet, consectetur adipiscing elit, sed do eiusmod tempor incididunt ut labore et dolore magna aliqua. Ut enim ad minim veniam, quis nostrud exercitation ullamco laboris nisi ut aliquip ex ea commodo consequat. Duis aute irure dolor in reprehenderit in voluptate velit esse cillum dolore eu fugiat nulla pariatur. Excepteur sint occaecat cupidatat non proident, sunt in culpa qui officia deserunt mollit anim id est laborum</div>
  <div class="btn" style="left:160px;top:381px;width:129px;height:36px;font-size:15px">Read more</div>
</section>
<svg class="abs" style="left:0;top:2300px" width="1200" height="140" viewBox="0 0 1200 140" aria-hidden="true">
  <path d="M0 60 C40 110 160 130 360 110 C640 80 900 40 1200 40 L1200 140 L0 140Z" fill="#fff"/>
  <path d="M0 40 L0 60 C40 110 160 130 360 110 C640 80 900 40 1200 40 L1200 30 C900 30 640 70 360 100 C160 118 40 95 0 40Z" fill="#2f3a4f"/>
</svg>

<div class="sec-title" style="top:2452px;color:var(--ink)">Latest news</div>
<div class="rule" style="left:573px;top:2512px"></div>

<article class="news-card" style="left:150px">
  <div class="ph" style="background:linear-gradient(135deg,#8aa07a 0%,#c9a97e 50%,#5a6d4a 100%)" role="img" aria-label="Women at an outdoor community market stall"></div>
  <div class="date">10 APRIL 2025</div>
  <h3>LOREM IPSUM DOLOR SIT AMET, CONSECTETUR</h3>
  <p>Lorem ipsum dolor sit amet, consectetur adipiscing elit, sed do eiusmod tempor incididunt ut labore et dolore magna aliqua</p>
  <div class="btn">Read more</div>
</article>
<article class="news-card" style="left:455px">
  <div class="ph" style="background:linear-gradient(135deg,#c7b3a0 0%,#5f6f7c 50%,#b89a82 100%)" role="img" aria-label="Group of women gathered around a tablet"></div>
  <div class="date">10 APRIL 2025</div>
  <h3>LOREM IPSUM DOLOR SIT AMET, CONSECTETUR</h3>
  <p>Lorem ipsum dolor sit amet, consectetur adipiscing elit, sed do eiusmod tempor incididunt ut labore et dolore magna aliqua</p>
  <div class="btn">Read more</div>
</article>
<article class="news-card" style="left:764px">
  <div class="ph" style="background:linear-gradient(180deg,#7fb2e6 0%,#cfe2f4 55%,#6f8a5a 100%)" role="img" aria-label="Friends raising their arms together on a grassy hill"></div>
  <div class="date">10 APRIL 2025</div>
  <h3>LOREM IPSUM DOLOR SIT AMET, CONSECTETUR</h3>
  <p>Lorem ipsum dolor sit amet, consectetur adipiscing elit, sed do eiusmod tempor incididunt ut labore et dolore magna aliqua</p>
  <div class="btn">Read more</div>
</article>

<section class="cta" role="img" aria-label="City skyline at dusk behind call to action">
  <h2>Have questions? Ideas? Want to volunteer<br>or simply share your thoughts?</h2>
  <p>We're here to listen, collaborate, and move forward — together.</p>
  <div class="btn" style="left:531px;top:208px;width:138px;height:40px;font-size:15px">Contact us</div>
</section>
<section class="footer"></section>
<svg class="abs" style="left:0;top:3290px" width="1200" height="110" viewBox="0 0 1200 110" aria-hidden="true">
  <path d="M0 70 C200 0 460 10 700 40 C900 65 1080 65 1200 40 L1200 110 L0 110Z" fill="#fff"/>
  <path d="M0 80 C200 20 460 40 700 60 C900 80 1080 75 1200 60 L1200 110 L0 110Z" fill="#e9ecf1"/>
  <path d="M0 70 C200 0 460 10 700 40 C900 65 1080 65 1200 40" fill="none" stroke="#d7141c" stroke-width="7"/>
  <path d="M300 40 C500 40 700 70 900 78 C1040 82 1140 70 1200 60" fill="none" stroke="#d7141c" stroke-width="9"/>
</svg>

<div class="f-logo">HARBOR LIGHT</div>
<nav class="f-nav">
  <a style="left:148px">HOME</a><a style="left:223px">ABOUT</a><a style="left:301px">CANDIDATE</a>
  <a style="left:412px">COMMUNITY</a><a style="left:533px">NEWS</a><a style="left:599px">CONTACT</a>
</nav>
<div class="contact-item" style="left:148px">
  <div class="ic"><svg width="18" height="18" viewBox="0 0 24 24" fill="#fff"><path d="M6.6 10.8a15 15 0 0 0 6.6 6.6l2.2-2.2a1 1 0 0 1 1-.25 11.4 11.4 0 0 0 3.6.57 1 1 0 0 1 1 1V20a1 1 0 0 1-1 1A17 17 0 0 1 3 4a1 1 0 0 1 1-1h3.5a1 1 0 0 1 1 1c0 1.25.2 2.45.57 3.57a1 1 0 0 1-.25 1z"/></svg></div>
  <span>CALL US<br>555-014-2287</span>
</div>
<div class="contact-item" style="left:424px">
  <div class="ic"><svg width="18" height="14" viewBox="0 0 24 18" fill="#fff"><path d="M0 2l12 8 12-8V0H0z"/><path d="M0 5v13h24V5l-12 8z"/></svg></div>
  <span>EMAIL US<br>hello@harborlight.example</span>
</div>
<div class="abs" style="left:150px;top:3664px;width:514px;height:2px;background:var(--navy)"></div>
<div class="abs" style="left:151px;top:3703px;font-family:Montserrat,sans-serif;font-weight:500;font-size:11.5px;color:var(--ink)">FOLLOW US</div>
<div class="social" style="left:242px"></div>
<div class="social" style="left:271px"></div>
<div class="social" style="left:300px"></div>
<div class="social" style="left:329px"></div>
<div class="social" style="left:358px"></div>
<div class="abs" style="left:150px;top:3755px;font-family:Montserrat,sans-serif;font-weight:600;font-size:13px;color:var(--ink)">Copyright © 2025 All Rights Reserved</div>
<div class="ph" style="left:736px;top:3459px;width:314px;height:314px;border-radius:50%;background:radial-gradient(circle at 50% 40%,#9c8e7c 0%,#5b6f55 55%,#3a4a63 100%)" role="img" aria-label="Crowd of people gathered at an outdoor community event"></div>

</body>
</html>
```